Luxury Resort Complex needs a Power Point Shell

Working in our primary color palate (pms colors can be provided and seen on our web site www.thelumenvale.com) design a title page, chapter page, and three slide page templates that include our logo either screened into the background or somewhere on the page which we can use for internal and external power point presentations.

Target Market(s)

Internal and External constituents

Industry/Entity Type

Hotel

```html
<!DOCTYPE html>
<html lang="en">
<head>
<meta charset="UTF-8">
<title>You Matter — The Lumen Vale</title>
<link rel="stylesheet" href="https://fonts.googleapis.com/css2?family=Jost:wght@400&family=Marcellus&display=swap">
<style>
  :root {
    --paper: #f9f7f2;
    --ink: #1a1a1a;
    --gold: #b39a6b;
    --gold-faint: #e9e1cf;
    --accent: #ec7683;
  }
  * { margin: 0; padding: 0; box-sizing: border-box; }
  html, body { width: 1200px; height: 675px; overflow: hidden; background: var(--paper); }
  .slide {
    position: relative;
    width: 1200px;
    height: 675px;
    background: var(--paper);
    overflow: hidden;
    font-family: "Jost", "Helvetica Neue", Arial, sans-serif;
  }
  .slide-title {
    position: absolute;
    left: 119px;
    top: 56px;
    font-family: "Marcellus", "Optima", serif;
    font-weight: 400;
    font-size: 32px;
    letter-spacing: -0.3px;
    color: var(--gold);
  }
  .brand-watermark {
    position: absolute;
    left: 500px;
    top: 228px;
    width: 200px;
    height: 215px;
    display: flex;
    align-items: center;
    justify-content: center;
    text-align: center;
    font-family: "Jost", "Helvetica Neue", Arial, sans-serif;
    font-size: 26px;
    line-height: 1.2;
    color: var(--gold-faint);
  }
  .body-copy {
    position: absolute;
    left: 120px;
    top: 122px;
    font-size: 15.9px;
    line-height: 19.5px;
    color: var(--ink);
  }
  .body-copy span, .pull-quote span { display: block; white-space: nowrap; }
  .divider-line {
    position: absolute;
    left: 826.5px;
    top: 0;
    width: 1px;
    height: 125px;
    background: var(--accent);
  }
  .divider-dot {
    position: absolute;
    left: 824.5px;
    top: 122.5px;
    width: 5px;
    height: 5px;
    border-radius: 50%;
    background: var(--accent);
  }
  .pull-quote {
    position: absolute;
    left: 866px;
    top: 117px;
    font-size: 21.4px;
    line-height: 26.3px;
    letter-spacing: 0.3px;
    color: var(--gold);
  }
  .wave-band {
    position: absolute;
    left: 0;
    top: 534px;
    width: 1200px;
    height: 92px;
    background: linear-gradient(180deg, var(--paper) 0%, var(--gold-faint) 20%, var(--gold-faint) 80%, var(--paper) 100%);
    opacity: 0.7;
  }
</style>
</head>
<body>
<main class="slide">
  <h1 class="slide-title">You Matter</h1>

  <div class="brand-watermark" aria-hidden="true">The Lumen Vale</div>

  <div class="body-copy">
    <span>Lorem ipsum dolor sit amet, consectetuer adipiscing elit, sed diam nonummy nibh euismod tin-</span>
    <span>cidunt ut laoreet dolore magna aliquam erat volutpat. Ut wisi enim ad minim veniam, quis nos-</span>
    <span>trud exerci tation ullamcorper suscipit lobortis nisl ut aliquip ex ea commodo consequat. Duis</span>
    <span>autem vel eum iriure dolor in hendrerit in vulputate velit esse molestie consequat, vel illum</span>
    <span>dolore eu feugiat nulla facilisis at vero eros et accumsan et iusto odio dignissim qui blandit</span>
    <span>praesent luptatum zzril delenit augue duis dolore te feugait nulla facilisi.</span>
    <span>Lorem ipsum dolor sit amet, cons ectetuer adipiscing elit, sed diam nonummy nibh euismod</span>
    <span>tincidunt ut laoreet dolore magna aliquam erat volutpat. Ut wisi enim ad minim veniam, quis</span>
    <span>nostrud exerci tation ullamcorper suscipit lobortis nisl ut aliquip ex ea commodo consequat.</span>
    <span>Lorem ipsum dolor sit amet, consectetuer adipiscing elit, sed diam nonummy nibh euismod tin-</span>
    <span>cidunt ut laoreet dolore magna aliquam erat volutpat. Ut wisi enim ad minim veniam, quis nos-</span>
    <span>trud exerci tation ullamcorper suscipit lobortis nisl ut aliquip ex ea commodo consequat. Duis</span>
    <span>autem vel eum iriure dolor in hendrerit in vulputate velit esse molestie consequat, vel illum</span>
    <span>dolore eu feugiat nulla facilisis at vero eros et accumsan et iusto odio dignissim qui blandit</span>
    <span>praesent luptatum zzril delenit augue duis dolore te feugait nulla facilisi.</span>
    <span>Lorem ipsum dolor sit amet, cons ectetuer adipiscing elit, sed diam nonummy nibh euismod</span>
    <span>tincidunt ut laoreet dolore magna aliquam erat volutpat. Ut wisi enim ad minim veniam, quis</span>
    <span>nostrud exerci tation ullamcorper suscipit lobortis nisl ut aliquip ex ea commodo consequat.</span>
    <span>Lorem ipsum dolor sit amet, consectetuer adipiscing elit, sed diam nonummy nibh euismod tin-</span>
  </div>

  <div class="divider-line"></div>
  <div class="divider-dot"></div>

  <div class="pull-quote">
    <span>Lorem ipsum dolor sit</span>
    <span>amet, consectetuer adipi-</span>
    <span>scing elit, sed diam</span>
    <span>nonummy nibh euismod</span>
    <span>tincidunt ut laoreet dolore</span>
    <span>magna aliquam erat vo-</span>
    <span>lutpat. Ut wisi enim ad</span>
    <span>minim veniam, quis nos-</span>
    <span>trud exerci tation ullam-</span>
    <span>corper suscipit lobortis</span>
    <span>nisl ut aliquip ex ea com-</span>
    <span>modo consequat. Duis</span>
    <span>autem vel eum iriure</span>
    <span>dolor in hendrerit in vul-</span>
  </div>

  <div class="wave-band" role="img" aria-label="Decorative band of fine gold wavy lines"></div>
</main>
</body>
</html>
```